全国の1人〜2人で営業されている理・美容室のオーナーさん方にコロナでも全く影響を受けてない当サロンのノウハウを読んで頂きたいと思っています。
これからのサロンのあり方、考え方、今すぐに取り入れるべき技術や商品、売り上げの上げ方などをお伝えします。本気で環境を変えたい方、美容師の仕事、接客、人をキレイにすることが大好きな方、意識の高いお客様に囲まれずっと通って頂けるような、そんな美容室を一緒に作って行きたいです。

この度はご提案、修正と本当にありがとうございました。最後の最後までかなり悩みました。
初めての電子書籍で良い表紙デザインと出会うことが出来ました。

今回、ご提案頂いた皆さん、本当にありがとうございました。初心者の自分に親身になって頂き、皆さんの丁寧なデザインに感動しました。また2冊目も考えています。ご縁があればまたよろしくお願いします。

```html
<!DOCTYPE html>
<html lang="ja">
<head>
<meta charset="utf-8">
<title>これからサロンが生き残る方法</title>
<link href="https://fonts.googleapis.com/css2?family=M+PLUS+Rounded+1c:wght@500;700;800;900&display=swap" rel="stylesheet">
<style>
  :root {
    --paper: #ffffff;
    --ink: #3a3a30;
    --accent-green: #5f7f3c;
    --highlight: #dfe58a;
    --band: #6e5b48;
    --band-text: #ffffff;
    --band-yellow: #f3e27a;
  }
  * { margin: 0; padding: 0; box-sizing: border-box; }
  html, body { width: 750px; height: 1200px; overflow: hidden; background: var(--paper); }
  .cover {
    position: relative; width: 750px; height: 1200px; overflow: hidden;
    background: var(--paper);
    font-family: "M PLUS Rounded 1c", sans-serif; color: var(--ink);
  }
  .kicker {
    position: absolute; left: 0; width: 750px; text-align: center;
    font-weight: 900; font-size: 72px; letter-spacing: 2px; line-height: 1;
  }
  .kicker span {
    background: linear-gradient(transparent 58%, var(--highlight) 58%, var(--highlight) 92%, transparent 92%);
    padding: 0 6px;
  }
  .kicker--one { top: 42px; }
  .kicker--two { top: 122px; }
  .from-now {
    position: absolute; left: 72px; top: 210px; width: 166px; height: 166px;
    border-radius: 50%; background: var(--accent-green); color: #fff;
    display: flex; flex-direction: column; align-items: center; justify-content: center;
    font-weight: 800; font-size: 50px; line-height: 1.1;
  }
  .title-salon {
    position: absolute; left: 250px; top: 232px;
    font-weight: 900; font-size: 112px; letter-spacing: 2px; line-height: 1;
  }
  .title-survive {
    position: absolute; left: 0; width: 750px; top: 375px; text-align: center;
    font-weight: 900; font-size: 112px; letter-spacing: 2px; line-height: 1;
  }
  .photo {
    position: absolute; left: 0; top: 512px; width: 750px; height: 415px;
    background: linear-gradient(100deg, #d9dbd6 0%, #eef0ec 30%, #c9b9a5 52%, #f2f2ef 70%, #dfe2df 100%);
  }
  .author {
    position: absolute; right: 28px; top: 528px;
    font-weight: 800; font-size: 40px; letter-spacing: 3px; color: var(--ink);
  }
  .band {
    position: absolute; left: 0; top: 927px; width: 750px; height: 273px;
    background: var(--band); padding: 28px 24px 0;
    font-weight: 700; font-size: 32.5px; line-height: 1.5; letter-spacing: 0.5px;
  }
  .band p { white-space: nowrap; }
  .band .lead { color: var(--band-text); }
  .band .target { color: var(--band-yellow); font-size: 31px; }
</style>
</head>
<body>
  <main class="cover">
    <h2 class="kicker kicker--one"><span>コロナや景気に</span></h2>
    <h2 class="kicker kicker--two"><span>左右されない</span></h2>
    <div class="from-now"><span>これ</span><span>から</span></div>
    <h1 class="title-salon">サロンが</h1>
    <h1 class="title-survive">生き残る方法</h1>
    <div class="photo" role="img" aria-label="明るい美容室の店内で腕を組んで微笑む女性美容師の写真"></div>
    <p class="author">たかはし みさき 著</p>
    <section class="band">
      <p class="lead">コロナ禍でも影響を受けていない当サロンの</p>
      <p class="lead">考え方や,これからの美容室のあり方、</p>
      <p class="lead">早急に準備すべき技術や商品をお伝え。</p>
      <p class="target">美容室経営者、これから独立したい美容師さん、</p>
      <p class="target">独自性が欲しいサロンさんのために・・・。</p>
    </section>
  </main>
</body>
</html>
```